Lumenfield Holdings

Professional looking business card using darker colours
I do not yet have a logo for the company so feel free to suggest
The business is based on consultancy and project management
Based in Melbourne
Business card can omit the word "Holdings" and can be Lumenfield consulting etc.

Business

Contact Name on card : Tom Verisco Contact number : +61412 305 617 Email address will be confirmed shortly.

```html
<!DOCTYPE html>
<html lang="en">
<head>
<meta charset="utf-8">
<title>Lumenfield Consulting – Business Card</title>
<link rel="stylesheet" href="https://fonts.googleapis.com/css2?family=Exo+2:wght@300;400&display=swap">
<style>
  :root {
    --page: #e9edf0;
    --card-black: #050607;
    --navy: #0a0f6e;
    --royal: #1c3fd0;
    --sky: #3fb3ea;
    --accent-line: #2050e0;
    --text-grey: #9aa0a8;
    --text-white: #ffffff;
    --text-blue: #2a5be8;
  }
  * { box-sizing: border-box; margin: 0; padding: 0; }
  html, body { width: 1200px; height: 1200px; overflow: hidden; }
  body {
    background: var(--page);
    font-family: "Exo 2", sans-serif;
    display: flex;
    flex-direction: column;
    align-items: center;
    justify-content: center;
    gap: 60px;
  }
  .card {
    position: relative;
    width: 860px;
    height: 491px;
    border-radius: 18px;
    background: var(--card-black);
    overflow: hidden;
    box-shadow: 0 6px 22px rgba(0,0,0,0.12);
  }

  /* ---------- Front ---------- */
  .front .sky-panel {
    position: absolute;
    left: 0; top: 0;
    width: 100%; height: 62%;
    background: radial-gradient(ellipse 90% 130% at 85% 100%, var(--sky) 0%, var(--royal) 45%, var(--navy) 100%);
  }
  .front .edge-line {
    position: absolute;
    left: 50px; top: 0;
    width: 7px; height: 62%;
    background: var(--accent-line);
  }
  .front .contact {
    position: absolute;
    left: 40px; top: 66%;
    color: var(--text-grey);
    font-weight: 300;
    font-size: 25px;
    line-height: 1.3;
    letter-spacing: 0.5px;
  }
  .front .contact .label {
    display: inline-block;
    width: 24px;
    color: var(--text-blue);
    font-weight: 400;
    font-size: 18px;
  }
  .front .contact .name { padding-left: 24px; }
  .front .company-name {
    position: absolute;
    right: 44px;
    top: 218px;
    color: var(--text-white);
    font-weight: 400;
    font-size: 40px;
    line-height: 1;
    letter-spacing: 0.5px;
  }

  /* ---------- Back ---------- */
  .back .tag-band {
    position: absolute;
    left: 0; bottom: 0;
    width: 100%; height: 17%;
    background: linear-gradient(90deg, var(--navy) 0%, var(--royal) 45%, var(--sky) 100%);
    display: flex;
    align-items: center;
    padding-left: 40px;
  }
  .back .tagline {
    color: var(--text-white);
    font-weight: 400;
    font-size: 25px;
    letter-spacing: 0.5px;
  }
  .back .edge-line {
    position: absolute;
    right: 48px; bottom: 0;
    width: 7px; height: 42%;
    background: var(--accent-line);
  }
  .back .about {
    position: absolute;
    left: 40px; top: 36px;
    width: 470px;
    color: var(--text-grey);
    font-weight: 300;
    font-size: 20px;
    line-height: 1.3;
  }
  .back .services {
    position: absolute;
    left: 540px; top: 160px;
    color: var(--text-grey);
    font-weight: 300;
    font-size: 21px;
    line-height: 1.3;
  }
  .back .services h2 {
    font-weight: 400;
    font-size: 21px;
    color: var(--text-white);
    margin-bottom: 6px;
  }
  .back .services ul { list-style: none; }
  .back .services li::before { content: "· "; }
</style>
</head>
<body>

  <section class="card front" aria-label="Business card front">
    <div class="sky-panel"></div>
    <div class="edge-line"></div>
    <div class="company-name">Lumenfield Consulting</div>
    <div class="contact">
      <div class="name">Tom Verisco</div>
      <div><span class="label">M</span>+61412 305 617</div>
      <div><span class="label">E</span>tom.verisco@lumenfield.com</div>
    </div>
  </section>

  <section class="card back" aria-label="Business card back">
    <p class="about">Consulting on omnihil audisquam, omnihic iliquat molorec torendae quaest, eaquis qui que que ex es Odigenia exerum voluptaquo magnaturi quam unt re solum qui corro magnihi tincid que ipsum que Odigenia exerum voluptaquo magnaturi quam unt re solum qui corro magnihi tincid que.</p>
    <div class="services">
      <h2>Expect the right expertise<br>for your business</h2>
      <ul>
        <li>Consultancy</li>
        <li>Management</li>
        <li>Training</li>
        <li>Skilled services</li>
        <li>International</li>
      </ul>
    </div>
    <div class="tag-band">
      <span class="tagline">Professional service with over 10 years experience</span>
    </div>
    <div class="edge-line"></div>
  </section>

</body>
</html>
```